Flyer für Kassensysteme
Zielgruppe
Kassensysteme - für diesen Flyer ist die Zielgruppe - Vereine - Unternehmen welche Vereinsfeste / Straßenfeste / Karnevalsitzungen oder Hausmessen bz. Messeverkäufe durchführen
Aufgabenstellung
optimal wäre DIN A5 einseitig welches auch so als Werbemail versendet werden kann. (unsere Internetpräsenz soll für diesen Firmenzweig von uns dann identisch angepasst werden) also ein schnell zu erfassender Flyer das es um Leih und Mietkassen für oben genannte Aktivitäten geht. kleiner Preis große Ersparnis Transparenz einfach zu bedienen

```html
<!DOCTYPE html>
<html lang="de">
<head>
<meta charset="utf-8">
<title>Leih- / Mietkassen – Kassora Datensysteme</title>
<link href="https://fonts.googleapis.com/css2?family=Montserrat:wght@400;500;700;800&display=swap" rel="stylesheet">
<style>
  :root {
    --navy: #3e5673;
    --steel: #92b3c8;
    --sky: #a9d0e6;
    --purple: #6b2a6e;
    --ink: #4a4a4a;
    --white: #ffffff;
    --stage: #c4c4c4;
  }
  * { margin: 0; padding: 0; box-sizing: border-box; }
  html, body { width: 1200px; height: 1200px; overflow: hidden; }
  body {
    background: var(--stage);
    font-family: "Montserrat", Arial, sans-serif;
    position: relative;
  }
  .flyer {
    position: absolute;
    left: 176px; top: 0;
    width: 848px; height: 1200px;
    background: var(--white);
    overflow: hidden;
  }
  .flyer-shapes { position: absolute; inset: 0; }
  .brand {
    position: absolute;
    top: 92px; left: 0; right: 0;
    display: flex; justify-content: center; align-items: center; gap: 16px;
    color: var(--navy);
    font-weight: 500;
    font-size: 30px;
    letter-spacing: 8px;
  }
  .brand-square { width: 40px; height: 40px; background: var(--navy); border-radius: 4px; }
  .product-visual {
    position: absolute;
    left: 81px; top: 207px;
    width: 683px; height: 446px;
    border-radius: 18px;
    background: radial-gradient(ellipse at 55% 45%, #5c6268 0%, #3a3d41 55%, rgba(58,61,65,0.0) 100%);
  }
  .headline {
    position: absolute; top: 686px; left: 0; right: 0;
    text-align: center;
    color: var(--purple);
    font-weight: 800;
    font-size: 64px;
    letter-spacing: 0.5px;
  }
  .subhead {
    position: absolute; top: 758px; left: 0; right: 0;
    text-align: center;
    color: var(--ink);
    font-weight: 700;
    font-size: 26px;
    line-height: 37px;
  }
  .body-copy {
    position: absolute; top: 859px; left: 0; right: 0;
    text-align: center;
    color: var(--ink);
    font-weight: 400;
    font-size: 17.5px;
    line-height: 26px;
  }
  .club-note {
    position: absolute; top: 974px; left: 114px;
    width: 618px; height: 46px;
    border-radius: 9px;
    background: var(--purple);
    color: var(--white);
    font-weight: 700;
    font-size: 16.5px;
    display: flex; align-items: center; justify-content: center;
  }
  .phone {
    position: absolute; top: 1040px; left: 0; right: 0;
    display: flex; justify-content: center; align-items: center; gap: 18px;
    color: var(--navy);
    font-weight: 700;
    font-size: 34px;
  }
  .phone-icon { width: 56px; height: 56px; }
  .web-address {
    position: absolute; top: 1138px; left: 0; right: 0;
    text-align: center;
    color: var(--white);
    font-weight: 700;
    font-size: 17px;
  }
</style>
</head>
<body>
<main class="flyer">
  <svg class="flyer-shapes" viewBox="0 0 848 1200" width="848" height="1200" aria-hidden="true">
    <path d="M0,200 Q424,330 848,162 L848,700 L0,700 Z" fill="var(--sky)"/>
    <path d="M0,216 Q424,348 848,182 L848,700 L0,700 Z" fill="var(--navy)"/>
    <path d="M0,686 Q360,548 848,592 L848,720 L0,720 Z" fill="var(--steel)"/>
    <path d="M0,702 Q360,566 848,610 L848,740 L0,740 Z" fill="var(--white)"/>
    <path d="M0,1180 H161 C205,1180 205,1113 255,1113 H603 C653,1113 653,1180 697,1180 H848 V1200 H0 Z" fill="var(--steel)"/>
  </svg>

  <div class="brand">
    <span class="brand-square"></span>
    <span class="brand-name">KASSORA DATENSYSTEME</span>
  </div>

  <div class="product-visual" role="img" aria-label="Kassensystem mit Touchscreen, Tastenfeld und Bondrucker"></div>

  <h1 class="headline">LEIH- / MIETKASSEN</h1>
  <p class="subhead">Sie planen bzw. veranstalten ein Vereinsfest eine<br>Hausmesse oder einen Sonderverkauf?</p>
  <p class="body-copy">Sparen Sie Zeit und Nerven mit der transparenten Abrechnung<br>über eine unserer Mietkassen - kinderleicht zu bedienen<br>und mit allen Funktionen eines modernen Kassensystems ausgestattet.</p>

  <div class="club-note">Für Vereine bieten wir unsere Leihkassen mit einer Miet-TSE an.</div>

  <div class="phone">
    <svg class="phone-icon" viewBox="0 0 56 56" aria-hidden="true">
      <circle cx="28" cy="28" r="28" fill="var(--navy)"/>
      <path d="M20.5 15.5c1.2-.8 2.6-.4 3.3.8l2 3.6c.6 1.1.3 2.4-.6 3.1l-1.6 1.2c1 2.6 3.3 5 5.9 6.2l1.3-1.6c.8-.9 2.1-1.1 3.1-.5l3.5 2.1c1.1.7 1.5 2.2.7 3.3l-1.3 1.9c-1 1.4-2.8 2-4.4 1.4-7.4-2.6-12.6-8-15-15.3-.5-1.6.1-3.3 1.5-4.3z" fill="var(--white)"/>
    </svg>
    <span class="phone-number">[0621] 48213-0</span>
  </div>

  <p class="web-address">https://www.kassora-verleih.de/leih-mietkassen/</p>
</main>
</body>
</html>
```